Strategic design partner needed for newly global technical consultancy! Starting with PowerPoint!

Veltrano.biz is a new consulting company offering technical assurance (reliability, business and cyber resiliency, operational excellence, and technical agility). We already have a logo (attached) and main font (Montserrat). Our colour scheme is gold and charcoal (color code of charcoal is #36454F, and for the gold is #B69904).
See the attachment for full colour palette we want! We need to partner with a designer for our corporate branding, starting with a PowerPoint deck that will be used for proposals and client meetings.
In a proposal deck we have items like Problem Statement (our joint understanding), Our Approach, Architecture, Timeline, Team, Assumptions/Dependencies/Risks, RACI, Pricing.
For corporate presentations we would have Introduction, Services, Methodology, Case Studies, Team, Clients, Contact.
This could lead to much more work. The website is just a placeholder, but we like the colours (veltrano dot biz)

Industry/Entity Type

Technology solutions apply across all industries. We have clients in fintech, pharma, retail, etc.

Requirements
Must have
• Match the colour scheme - SEE UPLOADED ATTACHMENT

```html
<!DOCTYPE html>
<html lang="en">
<head>
<meta charset="utf-8">
<title>Veltrano.biz Presentation Template</title>
<link rel="stylesheet" href="https://fonts.googleapis.com/css2?family=Montserrat:wght@300;400;500;600;700;800&display=swap">
<style>
:root{
  --charcoal:#36454F;
  --charcoal-dark:#2c3942;
  --band:#3c4a54;
  --gold:#B69904;
  --gold-light:#EBC34B;
  --gold-pale:#F3D57A;
  --ink:#333d44;
  --muted:#6f7880;
  --rule:#e2e2e2;
  --page:#ececec;
  --white:#fff;
}
*{box-sizing:border-box;margin:0;padding:0}
html,body{width:1200px;height:3099px;overflow:hidden}
body{background:var(--page);font-family:'Montserrat',sans-serif;color:var(--ink);position:relative}
.slide{position:absolute;width:540px;height:303px;background:var(--white);overflow:hidden;font-family:'Montserrat',sans-serif}
.hero{left:160px;top:84px;transform:scale(1.6296);transform-origin:0 0;box-shadow:0 4px 18px rgba(0,0,0,.18)}
.abs{position:absolute}
/* brand */
.brand{position:absolute;left:36px;top:28px;display:flex;align-items:center;gap:5px;font-weight:700;font-size:13px;color:var(--charcoal);letter-spacing:.3px}
.brand-mark{width:9px;height:9px;background:var(--gold)}
/* title slides */
.band{position:absolute;left:0;top:84px;width:540px;height:201px;background:linear-gradient(100deg,#3a4852 0%,#4a5760 55%,#56626b 100%)}
.band.light{background:linear-gradient(180deg,#f4f6f7 0%,#c5d0d8 100%)}
.deco{position:absolute;right:0;top:45px;width:245px;height:240px}
.t-title{position:absolute;left:36px;top:116px;color:var(--white);font-weight:800;font-size:23px;line-height:1.08}
.t-title span{font-weight:700}
.t-sub{position:absolute;left:36px;top:188px;color:var(--white);font-size:10.5px;font-weight:400}
.t-date{position:absolute;left:36px;top:230px;color:var(--white);font-size:5.5px;font-weight:500}
.dark-text .t-title,.dark-text .t-sub,.dark-text .t-date{color:var(--charcoal)}
.copy{position:absolute;left:0;right:0;top:291px;text-align:center;font-size:4.6px;letter-spacing:1px;color:#9aa0a5}
/* content */
.heading{position:absolute;left:0;right:0;top:26px;text-align:center;font-size:17px;font-weight:400;color:var(--charcoal)}
.heading b{font-weight:700}
.underline{position:absolute;left:242px;top:53px;width:56px;height:3px;background:var(--gold-light)}
.footer-rule{position:absolute;left:18px;right:18px;top:283px;height:4px;background:var(--rule)}
.footer-mark{position:absolute;left:18px;top:279px;width:10px;height:10px;background:var(--charcoal);border:2px solid var(--gold-light)}
.footer-copy{position:absolute;right:40px;top:282px;font-size:4px;letter-spacing:.6px;color:#8a9096;font-weight:600}
.page-no{position:absolute;right:20px;top:280px;width:10px;height:10px;border-radius:50%;background:var(--gold);color:#fff;font-size:5px;font-weight:700;text-align:center;line-height:10px}
.small{font-size:5.4px;line-height:1.35;color:var(--muted)}
.gold{color:var(--gold)}
.photo{position:absolute}
/* toc */
.toc-item{position:absolute;width:150px;height:40px}
.toc-num{position:absolute;left:0;top:0;font-size:20px;font-weight:300;color:#b9bdc0}
.toc-title{position:absolute;left:28px;top:2px;font-size:9.5px;color:var(--charcoal)}
.toc-title b{font-weight:700}
.toc-item.alt .toc-title{color:var(--gold)}
.toc-text{position:absolute;left:28px;top:15px;width:110px}
/* team */
.member{position:absolute;top:73px;width:100px;text-align:center}
.member .photo{position:relative;margin:0 auto;width:70px;height:100px;border:1.5px solid #fff;background:linear-gradient(180deg,#d9dcde,#9da4a9)}
.member h4{font-size:8.5px;font-weight:700;color:var(--charcoal);margin-top:7px}
.member .role{font-size:5.5px;color:var(--gold);margin-top:2px}
.member .small{margin-top:5px}
/* columns */
.col{position:absolute;top:70px;width:92px;text-align:center}
.col .tab{position:absolute;left:20px;top:5px;width:70px;height:18px;border-radius:0 9px 9px 0;background:#d7d7d7}
.col .ico{position:relative;margin-left:12px;width:29px;height:29px;border-radius:50%;background:var(--charcoal);border:3px solid #fff;box-shadow:0 0 0 1px #ccc}
.col.alt .ico{background:var(--gold)}
.col h5{font-size:8px;font-weight:700;color:var(--charcoal);margin-top:8px;line-height:1.1}
.col h5 span{font-weight:400}
.col.alt h5{color:var(--gold)}
.col .small{margin-top:8px}
.col-sep{position:absolute;top:70px;width:1px;height:185px;background:#eee}
/* steps */
.step{position:absolute;top:101px;width:90px;text-align:center}
.step .num{margin:0 auto;width:24px;height:24px;background:var(--charcoal);color:#fff;font-weight:700;font-size:11px;line-height:24px;clip-path:polygon(50% 0,100% 25%,100% 75%,50% 100%,0 75%,0 25%)}
.step.alt .num{background:var(--gold)}
.step h5{font-size:9px;font-weight:700;color:var(--charcoal);margin-top:13px;line-height:1.15}
.step h5 span{font-weight:400;display:block}
.step.alt h5{color:var(--gold)}
.step .small{margin-top:10px}
/* table */
.grid-table{position:absolute;left:28px;top:85px;width:484px;border-collapse:collapse;font-size:5.5px}
.grid-table th{height:15px;text-align:left;padding:0 4px;color:#fff;font-weight:700;font-size:6.5px}
.grid-table th:nth-child(1){background:var(--charcoal);width:98px}
.grid-table th:nth-child(2){background:var(--gold)}
.grid-table th:nth-child(3){background:var(--gold-light)}
.grid-table td{border-bottom:1px solid #ddd;vertical-align:top;padding:4px;height:44px}
.grid-table td:first-child{font-weight:700;color:var(--charcoal);font-size:6px;border-right:1px solid #ddd;vertical-align:middle}
.grid-table td b{display:block;font-size:6px;color:var(--charcoal);font-weight:600;margin-bottom:2px}
.grid-table ul{padding-left:8px;color:var(--muted);font-size:4.6px;line-height:1.3}
/* check list */
.checks{list-style:none;position:absolute;left:247px;top:118px;width:270px}
.checks li{position:relative;padding-left:12px;margin-bottom:6px;font-size:6.2px;line-height:1.3;color:var(--muted)}
.checks li::before{content:"";position:absolute;left:1px;top:1px;width:3px;height:5px;border:solid var(--gold);border-width:0 1.2px 1.2px 0;transform:rotate(45deg)}
.legend{position:absolute;left:345px;width:160px}
.legend h6{font-size:7px;font-weight:600;color:var(--charcoal);display:flex;align-items:center;gap:5px}
.legend .hex{width:10px;height:11px;clip-path:polygon(50% 0,100% 25%,100% 75%,50% 100%,0 75%,0 25%)}
.legend .small{padding-left:15px;margin-top:3px}
.contact{position:absolute;left:36px;list-style:none;color:#fff;font-size:6.5px}
.contact li{display:flex;align-items:center;gap:6px;margin-bottom:6px}
</style>
</head>
<body>

<!-- Hero title slide -->
<section class="slide hero">
  <div class="brand"><span class="brand-mark"></span>VELTRANO</div>
  <div class="band" role="img" aria-label="Muted office photograph behind the title"></div>
  <svg class="deco" viewBox="0 0 245 240" aria-hidden="true">
    <defs><linearGradient id="g1" x1="0" y1="0" x2="0" y2="1"><stop offset="0" stop-color="#3a4852"/><stop offset=".55" stop-color="#3a4852"/><stop offset=".56" stop-color="#d9a91d"/><stop offset="1" stop-color="#f4cb45"/></linearGradient></defs>
    <polygon points="0,110 145,0 245,62 245,240 0,240" fill="url(#g1)"/>
  </svg>
  <h1 class="t-title">PRESENTATION<br><span>Title Goes Here</span></h1>
  <p class="t-sub">Presentation Sub-Title Goes Here</p>
  <p class="t-date">Thursday, March 2, 2023</p>
  <p class="copy">Copyright © Veltrano. All Rights Reserved</p>
</section>

<!-- Row 1 -->
<section class="slide" style="left:51px;top:815px">
  <div class="brand"><span class="brand-mark"></span>VELTRANO</div>
  <div class="band" role="img" aria-label="Muted office photograph behind the title"></div>
  <svg class="deco" viewBox="0 0 245 240" aria-hidden="true">
    <defs><linearGradient id="g2" x1="0" y1="0" x2="0" y2="1"><stop offset="0" stop-color="#3a4852"/><stop offset=".55" stop-color="#3a4852"/><stop offset=".56" stop-color="#c8860a"/><stop offset="1" stop-color="#f4cb45"/></linearGradient></defs>
    <polygon points="0,110 145,0 245,62 245,240 0,240" fill="url(#g2)"/>
  </svg>
  <h1 class="t-title">PRESENTATION<br><span>Title Goes Here</span></h1>
  <p class="t-sub">Presentation Sub-Title Goes Here</p>
  <p class="t-date">Thursday, March 2, 2023</p>
  <p class="copy">Copyright © Veltrano. All Rights Reserved</p>
</section>

<section class="slide dark-text" style="left:609px;top:815px">
  <div class="brand"><span class="brand-mark"></span>VELTRANO</div>
  <div class="band light"></div>
  <svg class="deco" viewBox="0 0 245 240" aria-hidden="true">
    <polygon points="0,110 145,0 245,62 245,240 0,240" fill="url(#g2)"/>
  </svg>
  <h1 class="t-title">PRESENTATION<br><span>Title Goes Here</span></h1>
  <p class="t-sub">Presentation Sub-Title Goes Here</p>
  <p class="t-date">Thursday, March 2, 2023</p>
  <p class="copy">Copyright © Veltrano. All Rights Reserved</p>
</section>

<!-- Row 2 -->
<section class="slide" style="left:51px;top:1136px">
  <div class="brand"><span class="brand-mark"></span>VELTRANO</div>
  <div class="band" role="img" aria-label="Muted office photograph behind the title"></div>
  <svg class="deco" viewBox="0 0 245 240" aria-hidden="true">
    <polygon points="0,110 145,0 245,62 245,240 0,240" fill="#ffffff" opacity=".18"/>
  </svg>
  <h1 class="t-title">PRESENTATION<br><span>Title Goes Here</span></h1>
  <p class="t-sub">Presentation Sub-Title Goes Here</p>
  <p class="t-date">Thursday, March 2, 2023</p>
  <p class="copy">Copyright © Veltrano. All Rights Reserved</p>
</section>

<section class="slide" style="left:609px;top:1136px">
  <h2 class="heading">Table of <b>Contents</b></h2>
  <div class="underline"></div>
  <div class="toc-item" style="left:40px;top:98px"><span class="toc-num">1</span><p class="toc-title"><b>Title</b> Goes Here</p><p class="toc-text small">Lorem ipsum dolor sit amet, consectetur adipiscing elit.</p></div>
  <div class="toc-item alt" style="left:200px;top:98px"><span class="toc-num">2</span><p class="toc-title"><b>Title</b> Goes Here</p><p class="toc-text small">Lorem ipsum dolor sit amet, consectetur adipiscing elit.</p></div>
  <div class="toc-item" style="left:362px;top:98px"><span class="toc-num">3</span><p class="toc-title"><b>Title</b> Goes Here</p><p class="toc-text small">Lorem ipsum dolor sit amet, consectetur adipiscing elit.</p></div>
  <div class="toc-item alt" style="left:40px;top:151px"><span class="toc-num">4</span><p class="toc-title"><b>Title</b> Goes Here</p><p class="toc-text small">Lorem ipsum dolor sit amet, consectetur adipiscing elit.</p></div>
  <div class="toc-item" style="left:200px;top:151px"><span class="toc-num">5</span><p class="toc-title"><b>Title</b> Goes Here</p><p class="toc-text small">Lorem ipsum dolor sit amet, consectetur adipiscing elit.</p></div>
  <div class="toc-item alt" style="left:362px;top:151px"><span class="toc-num">6</span><p class="toc-title"><b>Title</b> Goes Here</p><p class="toc-text small">Lorem ipsum dolor sit amet, consectetur adipiscing elit.</p></div>
  <div class="toc-item" style="left:40px;top:204px"><span class="toc-num">7</span><p class="toc-title"><b>Title</b> Goes Here</p><p class="toc-text small">Lorem ipsum dolor sit amet, consectetur adipiscing elit.</p></div>
  <div class="toc-item alt" style="left:200px;top:204px"><span class="toc-num">8</span><p class="toc-title"><b>Title</b> Goes Here</p><p class="toc-text small">Lorem ipsum dolor sit amet, consectetur adipiscing elit.</p></div>
  <div class="toc-item" style="left:362px;top:204px"><span class="toc-num">9</span><p class="toc-title"><b>Title</b> Goes Here</p><p class="toc-text small">Lorem ipsum dolor sit amet, consectetur adipiscing elit.</p></div>
  <div class="footer-rule"></div><div class="footer-mark"></div>
  <p class="footer-copy">Copyright © Veltrano. All Rights Reserved</p><span class="page-no">4</span>
</section>

<!-- Row 3 -->
<section class="slide" style="left:51px;top:1459px">
  <div class="photo" style="left:23px;top:0;width:198px;height:248px;background:linear-gradient(160deg,#c9ced2,#7d868c 60%,#4e565c)" role="img" aria-label="Photo of a business handshake over a desk with a laptop"></div>
  <h3 class="abs" style="left:247px;top:24px;font-size:17px;font-weight:400;color:var(--charcoal)"><b style="font-weight:700">Heading</b> Goes Here</h3>
  <p class="abs" style="left:247px;top:72px;width:265px;font-size:7px;line-height:1.25;color:var(--gold)">Lorem ipsum dolor sit amet, consectetur adipiscing elit. Vivamus eu dui ex. Curabitur dapibus dignissim dui, in molestie metus feugiat sed.</p>
  <ul class="checks">
    <li>Lorem ipsum dolor sit amet, consectetur adipiscing elit. Vivamus eu dui ex.</li>
    <li>Curabitur dapibus dignissim dui, in molestie metus feugiat sed. Praesent aliquet lorem ex, eu dapibus odio varius at.</li>
    <li>Duis eget tellus porta, consequat lacus vitae, venenatis dolor. Nulla facilisi. In et sollicitudin lacus.</li>
    <li>Donec risus orci, gravida sit amet risus vehicula, aliquet pretium sapien. Nullam sit amet magna non ex bibendum mollis.</li>
    <li>Nunc vel neque eu augue dignissim congue ut vitae magna. Phasellus eget commodo arcu. Integer venenatis, tellus sit amet interdum pretium.</li>
  </ul>
  <div class="footer-rule"></div><div class="footer-mark"></div>
  <p class="footer-copy">Copyright © Veltrano. All Rights Reserved</p><span class="page-no">5</span>
</section>

<section class="slide" style="left:609px;top:1459px">
  <div class="abs" style="left:0;top:0;width:540px;height:142px;background:linear-gradient(100deg,#3a4852,#4f5c65)" role="img" aria-label="Muted photograph of a modern office ceiling"></div>
  <h2 class="heading" style="color:#fff">Meet Our <b>Team</b></h2>
  <div class="member" style="left:45px"><div class="photo" role="img" aria-label="Portrait of team member"></div><h4>Person Name</h4><p class="role">Job Title Goes Here</p><p class="small">Lorem ipsum dolor sit amet, consectetur adipiscing elit. Vivamus eu dui ex. Curabitur dapibus dignissim dui.</p></div>
  <div class="member" style="left:161px"><div class="photo" role="img" aria-label="Portrait of team member"></div><h4>Person Name</h4><p class="role">Job Title Goes Here</p><p class="small">Lorem ipsum dolor sit amet, consectetur adipiscing elit. Vivamus eu dui ex. Curabitur dapibus dignissim dui.</p></div>
  <div class="member" style="left:278px"><div class="photo" role="img" aria-label="Portrait of team member"></div><h4>Person Name</h4><p class="role">Job Title Goes Here</p><p class="small">Lorem ipsum dolor sit amet, consectetur adipiscing elit. Vivamus eu dui ex. Curabitur dapibus dignissim dui.</p></div>
  <div class="member" style="left:394px"><div class="photo" role="img" aria-label="Portrait of team member"></div><h4>Person Name</h4><p class="role">Job Title Goes Here</p><p class="small">Lorem ipsum dolor sit amet, consectetur adipiscing elit. Vivamus eu dui ex. Curabitur dapibus dignissim dui.</p></div>
  <div class="footer-rule"></div><div class="footer-mark"></div>
  <p class="footer-copy">Copyright © Veltrano. All Rights Reserved</p><span class="page-no">6</span>
</section>

<!-- Row 4 -->
<section class="slide" style="left:51px;top:1780px">
  <h2 class="heading"><b>Heading</b> Goes Here</h2>
  <div class="underline"></div>
  <div class="col-sep" style="left:141px"></div><div class="col-sep" style="left:237px"></div><div class="col-sep" style="left:333px"></div><div class="col-sep" style="left:429px"></div>
  <div class="col" style="left:45px"><span class="tab"></span><div class="ico"></div><h5>Lorem ipsum<br><span>dolor sit amet</span></h5><p class="small">Lorem ipsum dolor sit amet, consectetur adipiscing elit. Vivamus eu dui ex. Curabitur dapibus dignissim dui, in molestie metus feugiat sed. Praesent aliquet lorem ex, eu dapibus odio varius at. Vivamus eu dui ex.</p></div>
  <div class="col alt" style="left:141px"><span class="tab"></span><div class="ico"></div><h5>Lorem ipsum<br><span>dolor sit amet</span></h5><p class="small">Lorem ipsum dolor sit amet, consectetur adipiscing elit. Vivamus eu dui ex. Curabitur dapibus dignissim dui, in molestie metus feugiat sed. Praesent aliquet lorem ex, eu dapibus odio varius at. Vivamus eu dui ex.</p></div>
  <div class="col" style="left:237px"><span class="tab"></span><div class="ico"></div><h5>Lorem ipsum<br><span>dolor sit amet</span></h5><p class="small">Lorem ipsum dolor sit amet, consectetur adipiscing elit. Vivamus eu dui ex. Curabitur dapibus dignissim dui, in molestie metus feugiat sed. Praesent aliquet lorem ex, eu dapibus odio varius at. Vivamus eu dui ex.</p></div>
  <div class="col alt" style="left:333px"><span class="tab"></span><div class="ico"></div><h5>Lorem ipsum<br><span>dolor sit amet</span></h5><p class="small">Lorem ipsum dolor sit amet, consectetur adipiscing elit. Vivamus eu dui ex. Curabitur dapibus dignissim dui, in molestie metus feugiat sed. Praesent aliquet lorem ex, eu dapibus odio varius at. Vivamus eu dui ex.</p></div>
  <div class="col" style="left:429px"><span class="tab"></span><div class="ico"></div><h5>Lorem ipsum<br><span>dolor sit amet</span></h5><p class="small">Lorem ipsum dolor sit amet, consectetur adipiscing elit. Vivamus eu dui ex. Curabitur dapibus dignissim dui, in molestie metus feugiat sed. Praesent aliquet lorem ex, eu dapibus odio varius at. Vivamus eu dui ex.</p></div>
  <div class="footer-rule"></div><div class="footer-mark"></div>
  <p class="footer-copy">Copyright © Veltrano. All Rights Reserved</p><span class="page-no">7</span>
</section>

<section class="slide" style="left:609px;top:1780px">
  <h2 class="heading"><b>Heading</b> Goes Here</h2>
  <div class="underline"></div>
  <svg class="abs" style="left:180px;top:75px" width="180" height="175" viewBox="0 0 180 175" aria-hidden="true">
    <g transform="rotate(-90 90 87)" fill="none" stroke-width="44">
      <circle cx="90" cy="87" r="52" stroke="#36454F" stroke-dasharray="100 227" stroke-dashoffset="-8"/>
      <circle cx="90" cy="87" r="52" stroke="#B69904" stroke-dasharray="100 227" stroke-dashoffset="-117"/>
      <circle cx="90" cy="87" r="52" stroke="#F0C75E" stroke-dasharray="100 227" stroke-dashoffset="-226"/>
    </g>
    <circle cx="90" cy="87" r="26" fill="#fff"/>
    <rect x="81" y="78" width="18" height="18" fill="#36454F"/>
    <line x1="150" y1="20" x2="178" y2="20" stroke="#B69904" stroke-width="1"/><circle cx="150" cy="20" r="2" fill="#B69904"/>
    <line x1="150" y1="150" x2="178" y2="150" stroke="#B69904" stroke-width="1"/><circle cx="150" cy="150" r="2" fill="#B69904"/>
    <line x1="2" y1="43" x2="30" y2="43" stroke="#F0C75E" stroke-width="1"/><circle cx="30" cy="43" r="2" fill="#F0C75E"/>
  </svg>
  <div class="abs" style="left:55px;top:98px;width:120px;text-align:right"><p style="font-size:8px;color:var(--charcoal)"><b>Title</b> Goes Here</p><p class="small">Lorem ipsum dolor sit amet, consectetur adipiscing elit. Vivamus eu dui ex. Curabitur dapibus</p></div>
  <div class="abs" style="left:355px;top:76px;width:130px"><p style="font-size:8px;color:var(--charcoal)"><b>Title</b> Goes Here</p><p class="small">Lorem ipsum dolor sit amet, consectetur adipiscing elit. Vivamus eu dui ex. Curabitur dapibus</p></div>
  <div class="abs" style="left:355px;top:215px;width:130px"><p style="font-size:8px;color:var(--charcoal)"><b>Title</b> Goes Here</p><p class="small">Lorem ipsum dolor sit amet, consectetur adipiscing elit. Vivamus eu dui ex. Curabitur dapibus</p></div>
  <div class="footer-rule"></div><div class="footer-mark"></div>
  <p class="footer-copy">Copyright © Veltrano. All Rights Reserved</p><span class="page-no">8</span>
</section>

<!-- Row 5 -->
<section class="slide" style="left:51px;top:2101px">
  <h2 class="heading"><b>Heading</b> Goes Here</h2>
  <div class="underline"></div>
  <div class="abs" style="left:0;top:113px;width:520px;border-top:1px dotted #aaa"></div>
  <div class="step" style="left:41px"><div class="num">1</div><h5>Title<span>Goes Here</span></h5><p class="small">Lorem ipsum dolor sit amet, consectetur adipiscing elit. Vivamus eu dui ex. Curabitur dapibus dignissim dui, in molestie feugiat sed.</p></div>
  <div class="step alt" style="left:133px"><div class="num">2</div><h5>Title<span>Goes Here</span></h5><p class="small">Lorem ipsum dolor sit amet, consectetur adipiscing elit. Vivamus eu dui ex. Curabitur dapibus dignissim dui, in molestie feugiat sed.</p></div>
  <div class="step" style="left:225px"><div class="num">3</div><h5>Title<span>Goes Here</span></h5><p class="small">Lorem ipsum dolor sit amet, consectetur adipiscing elit. Vivamus eu dui ex. Curabitur dapibus dignissim dui, in molestie feugiat sed.</p></div>
  <div class="step alt" style="left:317px"><div class="num">4</div><h5>Title<span>Goes Here</span></h5><p class="small">Lorem ipsum dolor sit amet, consectetur adipiscing elit. Vivamus eu dui ex. Curabitur dapibus dignissim dui, in molestie feugiat sed.</p></div>
  <div class="step" style="left:409px"><div class="num">5</div><h5>Title<span>Goes Here</span></h5><p class="small">Lorem ipsum dolor sit amet, consectetur adipiscing elit. Vivamus eu dui ex. Curabitur dapibus dignissim dui, in molestie feugiat sed.</p></div>
  <div class="footer-rule"></div><div class="footer-mark"></div>
  <p class="footer-copy">Copyright © Veltrano. All Rights Reserved</p><span class="page-no">9</span>
</section>

<section class="slide" style="left:609px;top:2101px;background:linear-gradient(100deg,#3a4852 0%,#4c5962 60%,#66717a 100%)" role="img" aria-label="Muted photograph of a desk with charts and coffee">
  <svg class="deco" viewBox="0 0 245 240" style="top:63px" aria-hidden="true">
    <polygon points="0,110 145,0 245,62 245,240 0,240" fill="#ffffff" opacity=".15"/>
  </svg>
  <h2 class="abs" style="left:35px;top:126px;color:#fff;font-size:21px;font-weight:800;line-height:1.1">Section Break<br>Title Goes Here</h2>
  <p class="abs" style="left:35px;top:182px;color:#fff;font-size:9.5px">Sub-Title Goes Here</p>
</section>

<!-- Row 6 -->
<section class="slide" style="left:51px;top:2423px">
  <h2 class="heading"><b>Heading</b> Goes Here</h2>
  <div class="underline"></div>
  <p class="abs small" style="left:45px;top:72px;width:450px;text-align:center">Lorem ipsum dolor sit amet, consectetur adipiscing elit. Vivamus eu dui ex. Curabitur dapibus dignissim dui, in molestie metus feugiat sed. Praesent aliquet lorem ex, eu dapibus odio varius at. Lorem ipsum dolor sit amet, consectetur adipiscing elit. Vivamus eu dui ex. Curabitur dapibus dignissim dui, in molestie metus feugiat sed.</p>
  <svg class="abs" style="left:50px;top:112px" width="440" height="135" viewBox="0 0 440 135" aria-label="Bar chart of two trends by month">
    <g font-size="5" fill="#666" font-family="Montserrat, sans-serif" text-anchor="end">
      <text x="8" y="107">0</text><text x="8" y="97">0.5</text><text x="8" y="86">1</text><text x="8" y="76">1.5</text><text x="8" y="65">2</text><text x="8" y="55">2.5</text><text x="8" y="44">3</text><text x="8" y="34">3.5</text><text x="8" y="23">4</text><text x="8" y="13">4.5</text><text x="8" y="2">5</text>
    </g>
    <line x1="14" y1="105" x2="435" y2="105" stroke="#ccc" stroke-width=".6"/>
    <g fill="#36454F">
      <rect x="26" y="21" width="7" height="84"/><rect x="62" y="42" width="7" height="63"/><rect x="98" y="21" width="7" height="84"/><rect x="134" y="15" width="7" height="90"/><rect x="170" y="21" width="7" height="84"/><rect x="206" y="30" width="7" height="75"/><rect x="242" y="21" width="7" height="84"/><rect x="278" y="32" width="7" height="73"/><rect x="314" y="18" width="7" height="87"/><rect x="350" y="30" width="7" height="75"/><rect x="386" y="40" width="7" height="65"/><rect x="422" y="15" width="7" height="90"/>
    </g>
    <g fill="#B69904">
      <rect x="35" y="55" width="7" height="50"/><rect x="71" y="21" width="7" height="84"/><rect x="107" y="63" width="7" height="42"/><rect x="143" y="52" width="7" height="53"/><rect x="179" y="46" width="7" height="59"/><rect x="215" y="15" width="7" height="90"/><rect x="251" y="54" width="7" height="51"/><rect x="287" y="63" width="7" height="42"/><rect x="323" y="53" width="7" height="52"/><rect x="359" y="15" width="7" height="90"/><rect x="395" y="59" width="7" height="46"/><rect x="431" y="60" width="7" height="45"/>
    </g>
    <g font-size="5" fill="#666" font-family="Montserrat, sans-serif" text-anchor="middle">
      <text x="34" y="114">JAN</text><text x="70" y="114">FEB</text><text x="106" y="114">MAR</text><text x="142" y="114">APR</text><text x="178" y="114">MAY</text><text x="214" y="114">JUN</text><text x="250" y="114">JUL</text><text x="286" y="114">AUG</text><text x="322" y="114">SEP</text><text x="358" y="114">OCT</text><text x="394" y="114">NOV</text><text x="430" y="114">DEC</text>
      <rect x="182" y="123" width="3" height="3" fill="#36454F"/><text x="197" y="126">Trend 01</text>
      <rect x="213" y="123" width="3" height="3" fill="#B69904"/><text x="228" y="126">Trend 02</text>
    </g>
  </svg>
  <div class="footer-rule"></div><div class="footer-mark"></div>
  <p class="footer-copy">Copyright © Veltrano. All Rights Reserved</p><span class="page-no">11</span>
</section>

<section class="slide" style="left:609px;top:2423px">
  <h2 class="heading"><b>Heading</b> Goes Here</h2>
  <div class="underline"></div>
  <table class="grid-table">
    <tr><th>Heading</th><th>Title Goes Here</th><th>Title Goes Here</th></tr>
    <tr><td>Lorem ipsum dolor sit amet consectetur</td>
      <td><b>Heading Goes Here</b><ul><li>Lorem ipsum dolor sit amet, consectetur adipiscing elit.</li><li>Vivamus eu dui ex. Curabitur dapibus dignissim dui,</li><li>in molestie metus feugiat sed. Praesent aliquet lorem ex.</li></ul></td>
      <td><b>Heading Goes Here</b><ul><li>Lorem ipsum dolor sit amet, consectetur adipiscing elit.</li><li>Vivamus eu dui ex. Curabitur dapibus dignissim dui,</li><li>in molestie metus feugiat sed. Praesent aliquet lorem ex.</li></ul></td></tr>
    <tr><td>Lorem ipsum dolor sit amet consectetur</td>
      <td><b>Heading Goes Here</b><ul><li>Lorem ipsum dolor sit amet, consectetur adipiscing elit.</li><li>Vivamus eu dui ex. Curabitur dapibus dignissim dui,</li><li>in molestie metus feugiat sed. Praesent aliquet lorem ex.</li></ul></td>
      <td><b>Heading Goes Here</b><ul><li>Lorem ipsum dolor sit amet, consectetur adipiscing elit.</li><li>Vivamus eu dui ex. Curabitur dapibus dignissim dui,</li><li>in molestie metus feugiat sed. Praesent aliquet lorem ex.</li></ul></td></tr>
    <tr><td>Lorem ipsum dolor sit amet consectetur</td>
      <td><ul><li>Lorem ipsum dolor sit amet, consectetur adipiscing elit.</li><li>Vivamus eu dui ex. Curabitur dapibus dignissim dui,</li><li>in molestie metus feugiat sed. Praesent aliquet lorem ex.</li></ul></td>
      <td><ul><li>Lorem ipsum dolor sit amet, consectetur adipiscing elit.</li><li>Vivamus eu dui ex. Curabitur dapibus dignissim dui,</li><li>in molestie metus feugiat sed. Praesent aliquet lorem ex.</li></ul></td></tr>
  </table>
  <div class="footer-rule"></div><div class="footer-mark"></div>
  <p class="footer-copy">Copyright © Veltrano. All Rights Reserved</p><span class="page-no">12</span>
</section>

<!-- Row 7 -->
<section class="slide" style="left:51px;top:2744px">
  <h2 class="heading"><b>Heading</b> Goes Here</h2>
  <div class="underline"></div>
  <svg class="abs" style="left:40px;top:80px" width="230" height="110" viewBox="0 0 230 110" aria-label="Grouped bar chart of four categories">
    <g font-size="4.5" fill="#666" font-family="Montserrat, sans-serif" text-anchor="end">
      <text x="6" y="98">0</text><text x="6" y="82">1</text><text x="6" y="66">2</text><text x="6" y="50">3</text><text x="6" y="34">4</text><text x="6" y="18">5</text><text x="6" y="3">6</text>
    </g>
    <line x1="10" y1="96" x2="228" y2="96" stroke="#ccc" stroke-width=".6"/>
    <rect x="25" y="26" width="9" height="70" fill="#36454F"/><rect x="35" y="59" width="9" height="37" fill="#B69904"/><rect x="45" y="64" width="9" height="32" fill="#F3D57A"/>
    <rect x="80" y="56" width="9" height="40" fill="#36454F"/><rect x="90" y="26" width="9" height="70" fill="#B69904"/><rect x="100" y="64" width="9" height="32" fill="#F3D57A"/>
    <rect x="135" y="40" width="9" height="56" fill="#36454F"/><rect x="145" y="66" width="9" height="30" fill="#B69904"/><rect x="155" y="48" width="9" height="48" fill="#F3D57A"/>
    <rect x="190" y="24" width="9" height="72" fill="#36454F"/><rect x="200" y="40" width="9" height="56" fill="#B69904"/><rect x="210" y="16" width="9" height="80" fill="#F3D57A"/>
    <g font-size="4.5" fill="#666" font-family="Montserrat, sans-serif" text-anchor="middle">
      <text x="40" y="104">Category 1</text><text x="95" y="104">Category 2</text><text x="150" y="104">Category 3</text><text x="205" y="104">Category 4</text>
    </g>
  </svg>
  <p class="abs small" style="left:45px;top:210px;width:260px">Lorem ipsum dolor sit amet, consectetur adipiscing elit. Vivamus eu dui ex. Curabitur dapibus dignissim dui, in molestie metus feugiat sed. Praesent aliquet lorem ex, eu dapibus odio varius at. Duis eget tellus porta, consequat lacus vitae, venenatis dolor. Nulla facilisi. In et sollicitudin lacus. Donec risus orci, gravida sit amet risus vehicula, aliquet pretium sapien.</p>
  <div class="legend" style="top:78px"><h6><span class="hex" style="background:var(--charcoal)"></span>Heading Goes Here</h6><p class="small">Lorem ipsum dolor sit amet, consectetur adipiscing elit. Vivamus eu dui ex. Curabitur dapibus dignissim dui, in molestie metus feugiat sed.</p></div>
  <div class="legend" style="top:136px"><h6 class="gold"><span class="hex" style="background:var(--gold)"></span>Heading Goes Here</h6><p class="small">Lorem ipsum dolor sit amet, consectetur adipiscing elit. Vivamus eu dui ex. Curabitur dapibus dignissim dui, in molestie metus feugiat sed.</p></div>
  <div class="legend" style="top:194px"><h6 style="color:var(--gold-light)"><span class="hex" style="background:var(--gold-pale)"></span>Heading Goes Here</h6><p class="small">Lorem ipsum dolor sit amet, consectetur adipiscing elit. Vivamus eu dui ex. Curabitur dapibus dignissim dui, in molestie metus feugiat sed.</p></div>
  <div class="footer-rule"></div><div class="footer-mark"></div>
  <p class="footer-copy">Copyright © Veltrano. All Rights Reserved</p><span class="page-no">13</span>
</section>

<section class="slide" style="left:609px;top:2744px">
  <div class="brand"><span class="brand-mark"></span>VELTRANO</div>
  <div class="band" role="img" aria-label="Muted office photograph behind the closing message"></div>
  <svg class="deco" viewBox="0 0 245 240" aria-hidden="true">
    <polygon points="0,110 145,0 245,62 245,240 0,240" fill="#ffffff" opacity=".16"/>
  </svg>
  <h2 class="abs" style="left:36px;top:118px;color:var(--gold-light);font-size:21px;font-weight:800">Thank You!</h2>
  <p class="abs" style="left:36px;top:182px;color:#fff;font-size:9px;font-weight:700">Contact Us</p>
  <ul class="contact" style="top:203px">
    <li><svg width="7" height="7" viewBox="0 0 10 10"><path d="M2 1l2 2-1 1.5c.8 1.5 1.5 2.2 3 3L7.5 6l2 2-1.5 1.5C4.5 9 1 5.5.5 2.5z" fill="#fff"/></svg>Phone Number Goes Here</li>
    <li><svg width="7" height="7" viewBox="0 0 10 10"><circle cx="5" cy="5" r="4" fill="none" stroke="#fff" stroke-width="1.2"/><circle cx="5" cy="5" r="1.5" fill="#fff"/></svg>E-Mail Address Goes Here</li>
    <li><svg width="7" height="7" viewBox="0 0 10 10"><circle cx="5" cy="5" r="4" fill="none" stroke="#fff" stroke-width="1"/><ellipse cx="5" cy="5" rx="1.8" ry="4" fill="none" stroke="#fff" stroke-width=".8"/><line x1="1" y1="5" x2="9" y2="5" stroke="#fff" stroke-width=".8"/></svg>URL Address Goes Here</li>
  </ul>
  <p class="copy">Copyright © Veltrano. All Rights Reserved</p>
</section>

</body>
</html>
```